Business Card Design

Lanternfield Recruitment is a specialist financial services recruitment company and implementation partner

Industry/Entity Type

Business

Contact Information for Business Card

Tom Hadley
Lanternfield Recruiment Ltd
e:tom.hadley@lanternfield-recruitment.example
m:07723 408 316
m:07844 251 903
s: tommhadley

```html
<!DOCTYPE html>
<html lang="en">
<head>
<meta charset="utf-8">
<title>Lanternfield Recruitment – Business Card</title>
<link rel="stylesheet" href="https://fonts.googleapis.com/css2?family=Open+Sans:wght@400;600;700;800&display=swap">
<style>
  :root {
    --stage: #e9e6e2;
    --card-white: #ffffff;
    --card-black: #2a2a2b;
    --ink: #3c3c3e;
    --ink-soft: #8a8a8a;
    --charcoal: #474748;
    --accent: #d94a26;
    --rule: #9a9a9a;
    --mark-grey: #8d8b8c;
  }
  * { margin: 0; padding: 0; box-sizing: border-box; }
  html, body {
    width: 1200px; height: 900px; overflow: hidden;
    background: var(--stage);
    font-family: "Open Sans", Arial, sans-serif;
  }
  .stage { position: relative; width: 1200px; height: 900px; }
  .card {
    position: absolute; width: 680px; height: 400px; overflow: hidden;
    box-shadow: 0 10px 28px rgba(0,0,0,.22);
  }

  /* Back side */
  .card--back { left: 440px; top: 50px; background: var(--card-black); }
  .back-mark {
    position: absolute; left: 50%; top: 50%; width: 300px; height: 300px;
    transform: translate(-50%, -50%);
    border: 4px solid var(--mark-grey); border-radius: 50%;
    display: flex; align-items: center; justify-content: center;
  }
  .back-mark__name {
    color: var(--mark-grey); font-weight: 700; font-size: 22px;
    text-align: center; line-height: 1.3;
  }

  /* Front side */
  .card--front { left: 80px; top: 450px; background: var(--card-white); }
  .front-shapes { position: absolute; inset: 0; }
  .holder-name {
    position: absolute; left: 86px; top: 44px;
    font-size: 21px; font-weight: 700; color: var(--ink);
  }
  .holder-name__last { color: var(--accent); }

  .contacts {
    position: absolute; left: 52px; top: 188px; list-style: none;
    font-size: 16px; color: var(--ink); line-height: 26px;
  }
  .contacts__item { display: flex; align-items: center; gap: 10px; }
  .contacts__icon { width: 14px; height: 14px; flex: none; }

  .brand {
    position: absolute; left: 346px; top: 78px; width: 300px; text-align: center;
  }
  .brand__circle {
    width: 74px; height: 74px; margin: 0 auto 8px;
    border: 4px solid var(--accent); border-radius: 50%;
  }
  .brand__name {
    font-size: 22px; font-weight: 800; color: var(--ink); white-space: nowrap;
    line-height: 1.3;
  }
  .brand__rule { height: 1px; background: var(--rule); margin: 4px 0 2px; }
  .brand__suffix { font-size: 12px; color: var(--ink-soft); }
</style>
</head>
<body>
<main class="stage">

  <section class="card card--back" aria-label="Business card, back">
    <div class="back-mark">
      <span class="back-mark__name">Lanternfield<br>Recruitment</span>
    </div>
  </section>

  <section class="card card--front" aria-label="Business card, front">
    <svg class="front-shapes" width="680" height="400" viewBox="0 0 680 400" aria-hidden="true">
      <polygon points="0,0 48,0 34,26 0,26" fill="var(--charcoal)"/>
      <polygon points="52,0 60,0 46,26 30,26" fill="var(--accent)"/>
      <polygon points="0,300 0,332 270,378 296,350" fill="var(--charcoal)"/>
      <polygon points="300,400 318,334 680,392 680,400" fill="var(--accent)"/>
    </svg>

    <h1 class="holder-name">Tom <span class="holder-name__last">Hadley</span></h1>

    <ul class="contacts">
      <li class="contacts__item">
        <svg class="contacts__icon" viewBox="0 0 14 14" aria-hidden="true"><rect x="3" y="0.5" width="8" height="13" rx="1.5" fill="none" stroke="var(--accent)" stroke-width="1.6"/><circle cx="7" cy="11" r="0.9" fill="var(--accent)"/></svg>
        <span>07723 408 316</span>
      </li>
      <li class="contacts__item">
        <svg class="contacts__icon" viewBox="0 0 14 14" aria-hidden="true"><rect x="3" y="0.5" width="8" height="13" rx="1.5" fill="none" stroke="var(--accent)" stroke-width="1.6"/><circle cx="7" cy="11" r="0.9" fill="var(--accent)"/></svg>
        <span>07844 251 903</span>
      </li>
      <li class="contacts__item">
        <svg class="contacts__icon" viewBox="0 0 14 14" aria-hidden="true"><rect x="0.5" y="2.5" width="13" height="9" fill="var(--accent)"/><polyline points="0.5,2.5 7,8 13.5,2.5" fill="none" stroke="#fff" stroke-width="1.2"/></svg>
        <span>tom.hadley@lanternfield-recruitment.example</span>
      </li>
      <li class="contacts__item">
        <svg class="contacts__icon" viewBox="0 0 14 14" aria-hidden="true"><circle cx="7" cy="7" r="6.5" fill="var(--accent)"/></svg>
        <span>tommhadley</span>
      </li>
    </ul>

    <div class="brand">
      <div class="brand__circle"></div>
      <div class="brand__name">Lanternfield Recruitment</div>
      <div class="brand__rule"></div>
      <div class="brand__suffix">Ltd</div>
    </div>
  </section>

</main>
</body>
</html>
```